Bussines Card - RM EDIFICACIONES, S.A.

We need a design for a business card.
I want it to look professional, but not old fashion.
We are like "young people', somehow i want it to look fresh, new, different, but still serious and professional.
I could use, a non typical design. (I mean, not just rectangular design).

The company Name is " RM EDIFICACIONES, S.A. " we are Panamenian company (spanish language) dedicated to construction and civil engeniering.

The company logo is attached, i use it with white background. Im not sure trying different one, could try.

```html
<!DOCTYPE html>
<html lang="es">
<head>
<meta charset="utf-8">
<title>RM Edificaciones, S.A. — Tarjeta de presentación</title>
<link href="https://fonts.googleapis.com/css2?family=Open+Sans:wght@400;600;700&display=swap" rel="stylesheet">
<style>
  :root {
    --page: #e9e7e4;
    --card-front: #4b494a;
    --card-back: #5f5d5e;
    --mark-front: #6a6869;
    --name-front: #2e2d2d;
    --ink-light: #f2f2f2;
    --ink-soft: #cfcdcd;
    --rule: #8a8888;
  }
  * { box-sizing: border-box; margin: 0; padding: 0; }
  html, body { width: 1200px; height: 675px; overflow: hidden; }
  body {
    background: var(--page);
    font-family: "Open Sans", Arial, sans-serif;
    position: relative;
  }
  .card {
    position: absolute;
    top: 188px;
    width: 520px;
    height: 298px;
    border-radius: 3px;
    box-shadow: 0 6px 18px rgba(0,0,0,.18);
  }
  /* Front */
  .card--front { left: 60px; background: var(--card-front); }
  .front-mark {
    position: absolute;
    left: 218px; top: 58px;
    width: 96px; height: 96px;
    background: var(--mark-front);
  }
  .front-name {
    position: absolute;
    left: 0; right: 0; top: 196px;
    text-align: center;
    font-weight: 700;
    font-size: 25px;
    letter-spacing: 5px;
    color: var(--name-front);
  }
  /* Back */
  .card--back { left: 620px; background: var(--card-back); color: var(--ink-light); }
  .identity {
    position: absolute;
    left: 34px; top: 34px;
    display: flex; align-items: center; gap: 14px;
  }
  .identity-mark { width: 52px; height: 52px; background: var(--ink-light); }
  .identity-company { font-weight: 600; font-size: 13px; letter-spacing: 2px; }
  .person { position: absolute; left: 34px; top: 100px; }
  .person-name { font-weight: 600; font-size: 17px; letter-spacing: 2px; }
  .person-role { font-size: 9px; letter-spacing: 1.5px; color: var(--ink-soft); margin-top: 2px; }
  .divider {
    position: absolute;
    left: 232px; top: 150px;
    width: 1px; height: 110px;
    background: var(--rule);
  }
  .contact {
    position: absolute;
    left: 250px; top: 150px;
    list-style: none;
    font-size: 10px; letter-spacing: 1px; color: var(--ink-soft);
  }
  .contact li { display: flex; align-items: flex-start; gap: 8px; margin-bottom: 7px; line-height: 1.45; }
  .contact svg { flex: 0 0 11px; width: 11px; height: 11px; margin-top: 2px; fill: var(--ink-soft); }
</style>
</head>
<body>

<section class="card card--front" aria-label="Cara frontal">
  <div class="front-mark"></div>
  <p class="front-name">RM EDIFICACIONES, S.A.</p>
</section>

<section class="card card--back" aria-label="Cara posterior">
  <div class="identity">
    <div class="identity-mark"></div>
    <span class="identity-company">RM EDIFICACIONES, S.A.</span>
  </div>
  <div class="person">
    <p class="person-name">MATEO RIVAS</p>
    <p class="person-role">PRESIDENT &amp; CEO</p>
  </div>
  <div class="divider"></div>
  <ul class="contact">
    <li>
      <svg viewBox="0 0 12 12"><path d="M6 0a4 4 0 0 0-4 4c0 3 4 8 4 8s4-5 4-8a4 4 0 0 0-4-4zm0 5.6A1.6 1.6 0 1 1 6 2.4a1.6 1.6 0 0 1 0 3.2z"/></svg>
      <span>CALLE 50, BELLA VISTA, PLAZA MARBELLA,<br>2DO PISO LOCAL 4</span>
    </li>
    <li>
      <svg viewBox="0 0 12 12"><path d="M2.4 0.6l2 2.2-1 1.4a7 7 0 0 0 4.4 4.4l1.4-1 2.2 2-1.2 1.8C5.4 11.2 0.8 6.6 0.6 1.8z"/></svg>
      <span>390-1146</span>
    </li>
    <li>
      <svg viewBox="0 0 12 12"><rect x="3" y="0.5" width="6" height="11" rx="1"/></svg>
      <span>621 448-0273</span>
    </li>
    <li>
      <svg viewBox="0 0 12 12"><path d="M0 2h12v8H0zM0.8 2.6 6 6.6l5.2-4"/></svg>
      <span>MATEO@RMEDIFICA.COM</span>
    </li>
    <li>
      <svg viewBox="0 0 12 12"><circle cx="6" cy="6" r="5.5"/></svg>
      <span>WWW.RMEDIFICA.COM</span>
    </li>
  </ul>
</section>

</body>
</html>
```